Brochure Design Project for Q7

We are needing a brochure for our new company, Q7. We are based out of Columbus, Ohio. We are providing security for schools. We will be hiring veterans and former police officers to monitor schools and protect the children and staff.

Q7 Vision Statement:

To enable a safe and secure learning environment that will ensure prosperity and
possibility that our children deserve and with the parents peace of mind.

Q7 Mission Statement:

To empower our children and teachers by providing the world’s foremost security
professionals to preserve the learning environment from grades K-12. Q7 will actively
seek seasoned qualified security professionals to protect our children and teachers. We
will vet, train, deploy and manage our security professionals. We will strive to become the employer of choice for Security Professionals.

We would like our logo on the brochure with the following contact information:

phone number: 614-555-0192
email: Q7guarding@mailbox-example.com
(not sure of the website yet, I will send that to you when I get it)
address: P.O. Box 815, Larkfield Ohio 43990

We have established our website address and it is:  Q7guarding.example

We would like to have this on the flyer.

Our new email is:  mikeharwell#q7guarding.example
 
Could you please make these changes today because we have a mail out tomorrow.

```html
<!DOCTYPE html>
<html lang="en">
<head>
<meta charset="utf-8">
<title>Q7 – School Security Flyer</title>
<link rel="stylesheet" href="https://fonts.googleapis.com/css2?family=Mulish:wght@400;700;800&family=Arimo:wght@400;700&display=swap">
<style>
  :root {
    --paper: #ffffff;
    --gold-top: #c9b54a;
    --gold-mid: #7d7032;
    --charcoal: #2b2b2b;
    --charcoal-deep: #262626;
    --heading-gold: #f2c133;
    --body-gold: #e9d27c;
    --brand-gold: #d9b844;
    --contact-gold: #f0c14a;
    --contact-light: #d8d8d8;
    --band-gold: #b8a84a;
  }
  * { margin: 0; padding: 0; box-sizing: border-box; }
  html, body {
    width: 936px; height: 1200px; overflow: hidden; background: var(--paper);
  }
  .flyer {
    position: relative; width: 936px; height: 1200px; background: var(--paper);
  }
  .panel {
    position: absolute; left: 19px; top: 18px; width: 898px; height: 1162px;
    background: linear-gradient(180deg, var(--gold-top) 0%, var(--gold-mid) 14%, #3d3b33 32%, var(--charcoal) 48%, var(--charcoal-deep) 100%);
    overflow: hidden;
  }
  .brand-mark {
    position: absolute; left: 0; right: 0; top: 210px; text-align: center;
    font-family: "Mulish", sans-serif; font-weight: 800; font-size: 300px;
    line-height: 1; color: var(--brand-gold); letter-spacing: -6px;
  }
  .statements {
    position: absolute; left: 63px; top: 680px; width: 762px;
    font-family: "Mulish", sans-serif; color: var(--body-gold);
  }
  .statement + .statement { margin-top: 26px; }
  .statement-title {
    font-size: 18px; font-weight: 700; color: var(--heading-gold); line-height: 24px;
  }
  .statement-text {
    font-size: 19px; font-weight: 400; line-height: 25px;
  }
  .contact-band {
    position: absolute; left: 0; bottom: 0; width: 100%; height: 192px;
    background: linear-gradient(90deg, var(--charcoal-deep) 0%, var(--charcoal-deep) 22%, #4a4636 55%, var(--band-gold) 100%);
  }
  .band-mark {
    position: absolute; left: 66px; top: 42px; width: 110px; height: 110px;
    display: flex; align-items: center; justify-content: center;
    font-family: "Mulish", sans-serif; font-weight: 800; font-size: 62px;
    color: var(--brand-gold);
  }
  .contact {
    position: absolute; left: 227px; top: 50px;
    font-family: "Arimo", sans-serif; font-style: normal; color: var(--contact-light);
    font-size: 20px; line-height: 26px;
  }
  .contact-phone {
    font-weight: 700; font-size: 23px; line-height: 28px; color: var(--contact-gold);
  }
</style>
</head>
<body>
  <main class="flyer">
    <section class="panel">
      <div class="brand-mark">Q7</div>

      <div class="statements">
        <article class="statement">
          <h2 class="statement-title">Vision</h2>
          <p class="statement-text">To enable a safe and secure learning environment that will ensure prosperity and possibility that our children deserve and with the parents peace of mind.</p>
        </article>
        <article class="statement">
          <h2 class="statement-title">Mission</h2>
          <p class="statement-text">To empower our children and teachers by providing the world’s foremost security professionals to preserve the learning environment from grades K-12. Q7 will actively seek seasoned qualified security professionals to protect our children and teachers. We will vet, train, deploy and manage our security professionals. We will strive to become the employer of choice for Security Professionals.</p>
        </article>
      </div>

      <footer class="contact-band">
        <div class="band-mark">Q7</div>
        <address class="contact">
          <div class="contact-phone">614-555-0192</div>
          <div class="contact-email">mikeharwell#q7guarding.example</div>
          <div class="contact-web">Q7guarding.example</div>
          <div class="contact-address">P.O. Box 815, Larkfield Ohio 43990</div>
        </address>
      </footer>
    </section>
  </main>
</body>
</html>
```